Vel Oska Concrete Post Card Design Project

Hello, We are A Concrete Contractor. We specialize in removing and replacing concrete walkways, Patio's, Driveway's, ect., that are a trip hazard. We work a lot in Apartment complexes and Business Complexes where the trees have grown big and the roots from the trees lift up the concrete.
I would like someone to design a postcard (Two Sided) so I can send it out and market potential property manager customers. I would like to use our company logo on this card. Please see the pixel vault link below. Here are some things I would like the card to have on it.

1.Removal and Replacement of Concrete Sidewalks, Driveways, Parking Lots, Curb and Gutter.

2. ADA Compliant.

3. Repair of concrete tripping hazards and
root-damaged sidewalks.

4. Vel Oska Concrete brings your sidewalks in compliance with the Americans With Disabilities Act (ADA).

5. Property Management:

We cater to the needs of Property Mangement Companies, HOA, Apartment Complexes, Business Parks, Senior Living Complexes, Government Buildings and Shopping Centers.

6. Free Estimates
7. Contractors license number under our logo. It is:
BPLN #718390
8. Our phone numbers:555-284-9163 and 555-672-0394.

Card should be two sided 9" by 6"

Thank You
Updates

This website would not let me upload my logo so please click on the link below to get it.

 

http://i4471.pixelvault-host.com/albums/k218/Tvoska42/VelOskaConcreteLogo-2012-PROOF-2.jpg

Thank You

Reason: Hello, I have a lot of great designs. I have had a busy week and I am just now sitting down to ask for the changes I would like. Once I recieve all of the designs back with the changes I requested I would like to get the opinions of my coworkers and friends before selecting the design. I am asking for the deadline to be extended by 4 days. Thank You so much, Brenda Vel Oska

Target Market(s)

Property Managers

Industry/Entity Type

Concrete

Requirements
Must have
• Our logo

```html
<!DOCTYPE html>
<html lang="en">
<head>
<meta charset="utf-8">
<title>Vel Oska Concrete Postcard</title>
<link rel="stylesheet" href="https://fonts.googleapis.com/css2?family=Exo+2:wght@400;600;700;800&family=Saira+Semi+Condensed:wght@400;600&display=swap">
<style>
  :root {
    --page: #ffffff;
    --card-light: #f2f2f4;
    --hazard-yellow: #f9d616;
    --hazard-dark: #3a3a3a;
    --panel-grey: #5a5a5c;
    --panel-shade: #2e2e30;
    --brand-red: #d5202b;
    --text-dark: #222222;
    --text-grey: #777777;
    --logo-grey: #3c3c3c;
    --stripe-light: #e1e1e3;
  }
  * { box-sizing: border-box; margin: 0; padding: 0; }
  html, body { width: 1200px; height: 1000px; overflow: hidden; background: var(--page); }
  body { position: relative; font-family: "Exo 2", sans-serif; }

  .postcard {
    position: absolute;
    width: 605px;
    height: 430px;
    overflow: hidden;
    box-shadow: 2px 3px 6px rgba(60, 60, 110, 0.35);
  }
  .postcard--front { left: 55px; top: 55px; background: linear-gradient(#ffffff, #ececee); }
  .postcard--back { left: 550px; top: 522px; background: var(--card-light); }

  .postcard__art { position: absolute; left: 0; top: 0; }

  .hazard-band { position: absolute; left: 0; width: 100%; }
  .hazard-band--front {
    top: 50px; height: 60px;
    background: repeating-linear-gradient(120deg, var(--hazard-yellow) 0 34px, var(--hazard-dark) 34px 62px);
  }
  .hazard-band--back {
    top: 50px; height: 70px;
    background: repeating-linear-gradient(120deg, var(--stripe-light) 0 30px, var(--hazard-dark) 30px 58px);
  }

  .logo-plate {
    position: absolute; left: 52px; top: 22px; width: 233px; height: 156px;
    border: 4px solid var(--hazard-yellow); border-radius: 14px;
    background: #fff; padding: 6px;
  }
  .logo-plate__inner {
    width: 100%; height: 100%; border-radius: 10px;
    background: linear-gradient(#f4f4f4, #c9c9cb);
    display: flex; align-items: center; justify-content: center;
  }
  .brand-name {
    font-weight: 800; text-align: center; line-height: 1.02; text-transform: none;
  }
  .brand-name--front { color: var(--brand-red); font-size: 34px; }
  .brand-name--back {
    position: absolute; left: 40px; top: 150px; width: 240px;
    color: var(--logo-grey); font-size: 46px;
  }

  .license { position: absolute; text-align: center; letter-spacing: 0.5px; }
  .license--front { left: 52px; top: 184px; width: 233px; font-size: 14px; color: var(--text-grey); }
  .license--back { left: 40px; top: 296px; width: 240px; font-size: 20px; color: #444; }

  .badge-text {
    position: absolute; left: 383px; top: 52px; width: 110px;
    color: #fff; font-weight: 700; font-size: 21px; line-height: 1.05;
    text-align: center; transform: rotate(12deg);
  }

  .service-block { position: absolute; font-family: "Saira Semi Condensed", sans-serif; }
  .service-block__title { font-family: "Exo 2", sans-serif; font-weight: 700; font-size: 13px; }
  .service-block__body { font-size: 9.5px; line-height: 1.3; }
  .service-block--management { left: 24px; top: 288px; width: 220px; color: var(--text-dark); }
  .service-block--removal,
  .service-block--grinding { right: 22px; width: 300px; text-align: right; color: var(--hazard-yellow); }
  .service-block--removal { top: 296px; }
  .service-block--grinding { top: 352px; }

  .divider {
    position: absolute; left: 302px; top: 145px; width: 2px; height: 267px; background: var(--logo-grey);
  }
  .phones {
    position: absolute; left: 42px; top: 345px;
    font-size: 25px; font-weight: 600; line-height: 29px; color: var(--logo-grey);
  }
</style>
</head>
<body>

  <section class="postcard postcard--front" aria-label="Postcard front">
    <div class="hazard-band hazard-band--front"></div>

    <svg class="postcard__art" width="605" height="430" viewBox="0 0 605 430">
      <polygon class="starburst" transform="translate(438,100)" fill="#d21f2a"
        points="75,0 60.8,12.1 69.3,28.7 51.5,34.5 53,53 34.5,51.5 28.7,69.3 12.1,60.8 0,75 -12.1,60.8 -28.7,69.3 -34.5,51.5 -53,53 -51.5,34.5 -69.3,28.7 -60.8,12.1 -75,0 -60.8,-12.1 -69.3,-28.7 -51.5,-34.5 -53,-53 -34.5,-51.5 -28.7,-69.3 -12.1,-60.8 0,-75 12.1,-60.8 28.7,-69.3 34.5,-51.5 53,-53 51.5,-34.5 69.3,-28.7 60.8,-12.1"/>

      <rect x="0" y="207" width="605" height="223" fill="#ffffff"/>
      <g role="img" aria-label="Photo of a sidewalk cracked by tree roots">
        <rect x="0" y="207" width="115" height="58" fill="#7d8a6a"/>
      </g>
      <g role="img" aria-label="Photo of a tree trunk lifting a concrete path">
        <rect x="118" y="207" width="117" height="58" fill="#9a7f6c"/>
      </g>
      <g role="img" aria-label="Photo of a raised sidewalk slab beside a lawn">
        <polygon points="238,207 370,207 322,265 238,265" fill="#8fa36a"/>
      </g>
      <g role="img" aria-label="Photo of a worker finishing fresh concrete">
        <polygon points="376,207 485,207 485,273 326,273" fill="#8e8a86"/>
      </g>
      <g role="img" aria-label="Photo of a crew pouring a concrete slab">
        <rect x="488" y="207" width="117" height="66" fill="#a49c90"/>
      </g>

      <polygon points="326,276 605,276 605,430 220,430" fill="var(--panel-grey)"/>
      <polygon points="320,268 330,268 228,430 216,430 216,407" fill="var(--panel-shade)"/>
      <rect x="0" y="407" width="222" height="23" fill="#e4e4e6"/>
      <polygon points="0,268 322,268 218,407 0,407" fill="var(--hazard-yellow)"/>
    </svg>

    <div class="logo-plate">
      <div class="logo-plate__inner">
        <p class="brand-name brand-name--front">Vel Oska<br>Concrete</p>
      </div>
    </div>
    <p class="license license--front">BPLN #718390</p>

    <p class="badge-text">ADA Compliant Concrete</p>

    <div class="service-block service-block--management">
      <h2 class="service-block__title">Property Management:</h2>
      <p class="service-block__body">We cater to the needs of Property Mangement Companies, HOA, Apartment Complexes, Business Parks, Senior Living Complex, Government Buildings and Shopping Centers, concrete trip hazard repair and removal, sidewalk concrete repair.</p>
    </div>

    <div class="service-block service-block--removal">
      <h2 class="service-block__title">Removal and Replacement:</h2>
      <p class="service-block__body">Concrete Sidewalks, Driveways, Parking Lots, Curb and Gutters and ADA Compliant.</p>
    </div>

    <div class="service-block service-block--grinding">
      <h2 class="service-block__title">Concrete Grinding:</h2>
      <p class="service-block__body">Repair of tripping hazard removal, root-damaged sidewalks, 24 Hr Service. Vel Oska Concrete brings your sidewalks in compliance with the Americans With Disabilities Act (ADA)</p>
    </div>
  </section>

  <section class="postcard postcard--back" aria-label="Postcard back">
    <div class="hazard-band hazard-band--back"></div>
    <p class="brand-name brand-name--back">Vel Oska<br>Concrete</p>
    <p class="license license--back">BPLN #718390</p>
    <p class="phones">555-284-9163<br>555-672-0394</p>
    <div class="divider"></div>
  </section>

</body>
</html>
```